Watch brand needs new business cards

Kestrel Timepiece Company are looking for a new business card design incorporating our logo and brand colours as per our website.

Design should be 90x55mm with 3mm print margin from edges and 3mm external bleed.

Card should be double sided, e.g. logo one side, personal details on the other.

Logo will be provided as a vector.

The card must be able to show:
- Staff name
- Position
- Office Address
- Email
- Telephone number
- Website address

Final work must be provided in an editable format to allow us to add staff details (e.g. an AI or PSD file).

```html
<!DOCTYPE html>
<html lang="en">
<head>
<meta charset="utf-8">
<title>Kestrel Timepiece Company – Business Cards</title>
<link rel="stylesheet" href="https://fonts.googleapis.com/css2?family=Roboto:wght@400;500&display=swap">
<style>
  :root {
    --backdrop: #e2e2e2;
    --card: #f6f6f6;
    --ink: #231f20;
    --ink-soft: #2b2b2b;
    --band: #1e1b1c;
    --stripe: #4a4a4a;
    --paper-white: #ffffff;
    --card-shadow: 0 3px 6px rgba(0,0,0,0.28);
  }
  * { margin: 0; padding: 0; box-sizing: border-box; }
  html, body {
    width: 1200px; height: 576px; overflow: hidden;
    background: var(--backdrop);
    font-family: "Roboto", Arial, sans-serif;
    color: var(--ink);
  }
  .card {
    position: absolute;
    width: 484px; height: 292px;
    background: var(--card);
    border-radius: 6px;
    box-shadow: var(--card-shadow);
    overflow: hidden;
  }
  .card--front { left: 82px; top: 140px; }
  .card--back { left: 602px; top: 138px; }

  .brand { position: absolute; text-align: center; }
  .brand__circle {
    display: block; margin: 0 auto;
    border: 3px solid var(--ink); border-radius: 50%;
  }
  .brand__name {
    font-weight: 500; color: var(--ink);
    text-transform: uppercase; letter-spacing: 1.5px; line-height: 1.25;
  }
  .card--front .brand { left: 0; right: 0; top: 76px; }
  .card--front .brand__circle { width: 72px; height: 72px; margin-bottom: 18px; }
  .card--front .brand__name { font-size: 20px; }

  .card--back .brand { left: 22px; width: 220px; top: 68px; }
  .card--back .brand__circle { width: 92px; height: 92px; margin-bottom: 14px; }
  .card--back .brand__name { font-size: 14px; }

  .header-wave { position: absolute; left: 0; top: 0; width: 484px; height: 150px; }

  .person { position: absolute; right: 24px; top: 28px; text-align: right; color: var(--paper-white); }
  .person__name { font-size: 20px; font-weight: 500; letter-spacing: 0.3px; }
  .person__role { font-size: 11.5px; margin-top: 4px; }

  .address {
    position: absolute; left: 30px; top: 230px;
    font-size: 12.5px; line-height: 19px; color: var(--ink-soft);
  }
  .contacts {
    position: absolute; left: 264px; top: 209px;
    list-style: none; font-size: 12.5px; line-height: 18px; color: var(--ink-soft);
  }
  .contacts li { display: flex; align-items: center; }
  .contacts svg { width: 11px; height: 11px; margin-right: 12px; fill: var(--ink); }
</style>
</head>
<body>

<section class="card card--front" aria-label="Card front">
  <div class="brand">
    <span class="brand__circle"></span>
    <p class="brand__name">Kestrel Timepiece Company</p>
  </div>
</section>

<section class="card card--back" aria-label="Card back">
  <svg class="header-wave" viewBox="0 0 484 150" aria-hidden="true">
    <path d="M0 0 H484 V122 C420 120 350 96 275 58 C200 22 100 12 0 24 Z" fill="var(--band)"/>
    <path d="M0 60 C90 22 200 16 285 56 C360 92 420 126 484 140 V130 C420 122 360 96 292 64 C210 26 100 22 0 44 Z" fill="var(--stripe)"/>
    <path d="M40 62 C130 34 210 34 280 66 C230 44 140 40 40 62 Z" fill="var(--stripe)"/>
  </svg>

  <div class="person">
    <p class="person__name">Daniel Hart</p>
    <p class="person__role">Managing Director</p>
  </div>

  <div class="brand">
    <span class="brand__circle"></span>
    <p class="brand__name">Kestrel<br>Timepiece Company</p>
  </div>

  <p class="address">418 Harbor Lane<br>Lakeview Oregon 97000</p>

  <ul class="contacts">
    <li><svg viewBox="0 0 24 24" aria-hidden="true"><path d="M2 8 C2 4 7 3 12 3 S22 4 22 8 V10 H16 V7 H8 V10 H2 Z M5 12 H19 L21 21 H3 Z M12 14 A2.5 2.5 0 1 0 12 19 A2.5 2.5 0 1 0 12 14 Z"/></svg>+111 555 0147</li>
    <li><svg viewBox="0 0 24 24" aria-hidden="true"><path d="M12 2 A10 10 0 1 0 12 22 A10 10 0 1 0 12 2 Z M4.1 11 H8 C8.1 8.3 8.7 5.9 9.6 4.4 A8 8 0 0 0 4.1 11 Z M10 11 H14 C13.9 7.5 12.9 4.4 12 4 C11.1 4.4 10.1 7.5 10 11 Z M16 11 H19.9 A8 8 0 0 0 14.4 4.4 C15.3 5.9 15.9 8.3 16 11 Z M4.1 13 A8 8 0 0 0 9.6 19.6 C8.7 18.1 8.1 15.7 8 13 Z M10 13 C10.1 16.5 11.1 19.6 12 20 C12.9 19.6 13.9 16.5 14 13 Z M16 13 C15.9 15.7 15.3 18.1 14.4 19.6 A8 8 0 0 0 19.9 13 Z"/></svg>www.kestreltimepiece.com</li>
    <li><svg viewBox="0 0 24 24" aria-hidden="true"><path d="M2 5 H22 V19 H2 Z M4 7 L12 13 L20 7 Z"/></svg>daniel@kestreltimepiece.com</li>
  </ul>
</section>

</body>
</html>
```